Postcard Design - Simple

Freight Factoring Company - We purchase freight invoices from trucking companies. We then pay them the same day so they don't have to wait 4-6 weeks to get their money.

Industry/Entity Type

It Company

```html
<!DOCTYPE html>
<html lang="en">
<head>
<meta charset="utf-8">
<title>Haulway Partners Postcard</title>
<link rel="stylesheet" href="https://fonts.googleapis.com/css2?family=Oswald:wght@400;500&family=Jost:wght@400;600&display=swap">
<style>
  :root {
    --navy: #1f3466;
    --navy-deep: #172850;
    --white: #ffffff;
    --ink: #1b1b1b;
    --photo-light: #e4e5e7;
    --photo-mid: #a9abae;
    --photo-dark: #5c5f63;
    --panel: #e9eaec;
    --caption: #4a4a4a;
  }
  html, body { margin: 0; padding: 0; }
  body {
    width: 1200px; height: 900px; overflow: hidden;
    background: var(--white);
    font-family: "Jost", sans-serif;
  }
  .postcard { position: relative; width: 1200px; height: 900px; overflow: hidden; background: var(--white); }
  .postcard__shapes { position: absolute; inset: 0; }

  .brand-name {
    position: absolute; left: 80px; top: 52px; margin: 0;
    display: flex; align-items: center; gap: 16px;
    font-family: "Oswald", sans-serif; font-weight: 500;
    font-size: 46px; letter-spacing: 1px; text-transform: uppercase;
    color: var(--white);
  }
  .brand-name__dot { width: 22px; height: 22px; border-radius: 50%; background: var(--white); }

  .contact { position: absolute; right: 66px; top: 42px; text-align: right; font-family: "Oswald", sans-serif; color: var(--ink); }
  .contact__lead { margin: 0; font-size: 27px; font-weight: 400; }
  .contact__phone { margin: 0; font-size: 27px; font-weight: 400; line-height: 1.2; }
  .contact__number { font-size: 46px; font-weight: 500; color: var(--navy); }

  .slogan { position: absolute; left: 772px; top: 176px; margin: 0; font-family: "Oswald", sans-serif; color: var(--white); }
  .slogan__name { display: block; font-size: 28px; font-weight: 500; }
  .slogan__line { display: block; margin-left: 20px; font-size: 38px; font-weight: 500; line-height: 1.2; }

  .offer-title { position: absolute; right: 66px; top: 312px; margin: 0; text-align: right; font-family: "Oswald", sans-serif; font-weight: 500; color: var(--navy); }
  .offer-title__top { display: block; font-size: 34px; line-height: 1.15; }
  .offer-title__bottom { display: block; font-size: 28px; line-height: 1.25; }

  .offer-copy { position: absolute; left: 619px; top: 412px; width: 520px; margin: 0; font-size: 24px; line-height: 31px; color: var(--ink); }

  .why { position: absolute; left: 619px; top: 676px; width: 540px; }
  .why__title { margin: 0 0 6px; font-size: 32px; font-weight: 600; color: var(--navy); }
  .why__list { margin: 0; padding: 0; list-style: none; }
  .why__item { font-size: 23px; line-height: 33px; color: var(--ink); }
  .why__item::before { content: "\2022"; margin-right: 6px; }

  .newsletter {
    position: absolute; left: 222px; top: 700px; width: 362px; height: 76px;
    display: flex; align-items: center; gap: 14px; padding: 0 14px; box-sizing: border-box;
    background: var(--panel); border-radius: 8px;
  }
  .newsletter__mark { width: 40px; height: 40px; background: var(--navy); flex: none; }
  .newsletter__name { margin: 0; font-family: "Oswald", sans-serif; font-weight: 500; font-size: 22px; line-height: 1.15; text-transform: uppercase; color: var(--navy); }
  .newsletter__note { position: absolute; left: 246px; top: 782px; margin: 0; font-size: 16px; font-weight: 600; line-height: 1.15; color: var(--caption); }
</style>
</head>
<body>
<main class="postcard">
  <svg class="postcard__shapes" width="1200" height="900" viewBox="0 0 1200 900">
    <defs>
      <linearGradient id="trailer-tone" x1="0" y1="0" x2="1" y2="1">
        <stop offset="0" stop-color="var(--photo-light)"/>
        <stop offset="0.55" stop-color="var(--photo-mid)"/>
        <stop offset="1" stop-color="var(--photo-dark)"/>
      </linearGradient>
    </defs>
    <g role="img" aria-label="Photo of a white semi-trailer with its rear doors open, loaded with a large roll of cash">
      <polygon points="0,156 728,156 20,864 0,864" fill="url(#trailer-tone)"/>
    </g>
    <polygon class="band-top" points="0,0 884,0 728,156 0,156" fill="var(--navy)"/>
    <polygon class="band-diagonal" points="884,0 929,0 29,900 -16,900" fill="var(--navy)"/>
    <line x1="899" y1="0" x2="-1" y2="900" stroke="var(--white)" stroke-width="2" opacity="0.7"/>
    <polygon class="band-bottom" points="0,864 20,864 0,884" fill="var(--navy-deep)"/>
    <polygon class="band-slogan" points="763,166 1200,166 1200,276 653,276" fill="var(--navy)"/>
  </svg>

  <h1 class="brand-name"><span class="brand-name__dot"></span>Haulway Partners</h1>

  <div class="contact">
    <p class="contact__lead">Contact us today</p>
    <p class="contact__phone">at <span class="contact__number">555-014-2290</span></p>
  </div>

  <p class="slogan">
    <span class="slogan__name">Haulway Partners:</span>
    <span class="slogan__line">“WE Deliver Solutions”</span>
  </p>

  <h2 class="offer-title">
    <span class="offer-title__top">Turn Your</span>
    <span class="offer-title__bottom">Freight Bills Into Cash!</span>
  </h2>

  <p class="offer-copy">Haulway Partners Financial is a factoring company that specializes in the trucking industry. We understand CASH is “King of the Road” and you can't wait 30-45 days . . . or longer to get paid. You deserve to be paid as soon as you've delivered the load! Our freight factoring</p>

  <section class="why">
    <h3 class="why__title">Why Haulway Partners?</h3>
    <ul class="why__list">
      <li class="why__item">Unlimited Earning Potential</li>
      <li class="why__item">Low Start Up Cost</li>
      <li class="why__item">Work at Your Own Pace</li>
      <li class="why__item">Established Carrier Base</li>
      <li class="why__item">Sales &amp; Marketing Support</li>
    </ul>
  </section>

  <div class="newsletter">
    <span class="newsletter__mark"></span>
    <p class="newsletter__name">Haulway Partners<br>Newsletter</p>
  </div>
  <p class="newsletter__note">Fill out the form below<br>to receive our eNewsletter.</p>
</main>
</body>
</html>
```